Web Design for a Biotech Consulting Firm

We need a web site design for a new business based in Philadelphia called Corventa Dx. This is a consulting firm that will serve medical diagnostics industry, which is part of the life science/healthcare industry focusing on developing and marketing products that help in early detection, monitoring or management of diseases. Our consulting firm will help medical diagnostic companies to overcome key challenges in designing, evaluating and marketing new products.Our company name is Corventa Dx. Corventa is Latin word for "something" Dx represents diagnostics. The idea behind the name is that we help companies to transform the original, early product ideas ("nothing") into "something"; which is a product with full clinical utility that will help to improve health and well-being.The web site should use the visual feel of the logo (attached), be modern, simple and clean looking and represent creativity, innovation, scientific thinking and progress.
Updates

Wix Design is acceptable

Industry/Entity Type

Biotechnology

Coding

Coded - Design and coding required

Number of Pages Required

1 page

Font styles to use
Sans Serif

Requirements
Must have
• simple, clean look couple of pages
Should not have
• a lot of pages

```html
<!DOCTYPE html>
<html lang="en">
<head>
<meta charset="utf-8">
<title>Corventa Dx</title>
<link href="https://fonts.googleapis.com/css2?family=Montserrat:ital,wght@0,400;0,500;0,600;0,700;1,500&display=swap" rel="stylesheet">
<style>
:root{
  --blue:#1e88f0;
  --ink:#1a1a1a;
  --text:#333;
  --grey-bg:#f2f2f2;
  --line:#e2e2e2;
  --white:#fff;
}
*{box-sizing:border-box;margin:0;padding:0}
html,body{width:1200px;height:4979px;overflow:hidden}
body{font-family:"Montserrat",sans-serif;color:var(--text);background:var(--white);position:relative}
section,header,footer{position:absolute;left:0;width:1200px}
.abs{position:absolute}
.btn{position:absolute;background:var(--blue);color:#fff;font-weight:600;font-size:14px;display:flex;align-items:center;justify-content:center;border-radius:5px;letter-spacing:.5px}
.heading{position:absolute;left:50%;transform:translateX(-50%);font-size:30px;font-weight:700;color:var(--ink);padding:14px 18px;white-space:nowrap}
.heading::before{content:"";position:absolute;left:0;top:0;width:60%;height:100%;border-left:2px solid var(--blue);border-top:2px solid var(--blue)}
.heading span{color:var(--blue);font-weight:500}
.heading.left{transform:none}

/* header */
.topbar{position:absolute;right:0;top:0;width:530px;height:50px;background:var(--blue);color:#fff;font-size:14px;display:flex;align-items:center;gap:30px;padding-left:40px;clip-path:polygon(20px 0,100% 0,100% 100%,0 100%)}
.topbar .item{display:flex;align-items:center;gap:8px}
.topbar .social{display:flex;gap:6px;margin-left:auto;margin-right:22px}
.topbar .social i{width:22px;height:22px;border:1.5px solid #fff;border-radius:50%}
.brand{position:absolute;display:flex;align-items:center;gap:12px;font-size:26px;font-weight:500;color:var(--ink);white-space:nowrap}
.brand .mark{width:16px;height:16px;background:var(--blue)}
.nav{position:absolute;right:40px;top:78px;display:flex;gap:22px;font-size:12px;color:#444;align-items:center}
.nav .active{border:1.5px solid var(--blue);padding:12px 6px;font-weight:700;color:var(--ink)}

/* hero */
.hero{top:145px;height:597px;background:linear-gradient(135deg,#9fb6c6 0%,#d9e3ea 40%,#e9eef2 60%,#7b8f9f 100%)}
.hero p{position:absolute;left:80px;width:1040px;top:207px;text-align:center;font-weight:700;font-size:24px;line-height:1.35;color:#1a2630}

.about{top:742px;height:466px}
.body-text{position:absolute;left:100px;width:1000px;top:208px;text-align:center;font-size:15.5px;line-height:1.35;color:#333}

.services{top:1208px;height:590px;background:var(--grey-bg)}
.card{position:absolute;top:204px;width:304px}
.card .photo{height:187px}
.card h4{margin-top:30px;font-size:16px;font-weight:500;color:var(--blue)}
.card p{font-size:16px;line-height:1.3;color:#444}
.arrow{position:absolute}

.clients{top:1798px;height:356px}
.client-row{position:absolute;top:224px;left:160px;width:880px;display:flex;justify-content:space-between;align-items:center;font-weight:700;font-size:30px;color:#c4c4c4;letter-spacing:1px}

.news{top:2154px;height:996px;background:var(--grey-bg)}
.tile{position:absolute;background:#fff}
.tile .date{font-size:15px;color:var(--blue);font-weight:500}
.tile p{font-size:16px;line-height:1.35;color:#333}
.dot-arrow{width:22px;height:22px;margin-top:12px}
.all-news{display:flex;align-items:center;justify-content:center;text-align:center;font-weight:700;font-size:22px;color:var(--ink);line-height:1.2;letter-spacing:1px}

.testimonials{top:3150px;height:809px}
.quote{position:absolute;background:#fff;border:1px solid var(--line);border-radius:6px;box-shadow:0 2px 8px rgba(0,0,0,.08);padding:26px 30px;font-size:14.5px;line-height:1.5;color:#333}
.person{position:absolute;display:flex;align-items:center;gap:22px;font-style:italic;font-weight:500;font-size:17px;color:#333}
.avatar{width:92px;height:92px;border-radius:50%;border:3px solid var(--blue);background:radial-gradient(circle,#e8d3c1,#b89b86)}
.dots{position:absolute;left:563px;top:635px;display:flex;gap:6px}
.dots i{width:13px;height:13px;border:1.5px solid #999;border-radius:50%}
.dots i:first-child{background:#bbb}

.contact{top:3959px;height:473px;background:var(--grey-bg)}
.field{position:absolute;background:#fff;font-size:13px;color:#444;padding:0 16px;display:flex;align-items:center}
.field.msg{align-items:flex-start;padding-top:14px}
.info{position:absolute;left:871px;top:146px;font-size:16px;line-height:1.4;color:#222}
.info .row{display:flex;gap:12px;margin-bottom:28px}
.info svg{flex:none;margin-top:2px}

.footer{top:4432px;height:493px}
.col{position:absolute;top:253px;font-size:12.5px;color:#333;line-height:1.55}
.col h5{font-size:13px;font-weight:700;color:var(--ink);padding-bottom:10px;margin-bottom:12px;border-bottom:1px solid var(--line);width:100px}
.col .s{display:flex;align-items:center;gap:12px;margin-bottom:10px}
.col .s i{width:20px;height:20px;border-radius:50%;background:var(--blue)}
.subscribe-field{width:255px;height:28px;background:#eee;border-radius:14px;margin-top:18px;padding-left:16px;display:flex;align-items:center;font-size:12px;color:#555}
.copyright{top:4925px;height:54px;background:var(--blue);color:#fff;font-size:11px;font-weight:600;display:flex;align-items:center;justify-content:center;letter-spacing:.5px}
</style>
</head>
<body>

<header class="site-header" style="top:0;height:145px">
  <div class="topbar">
    <div class="item">
      <svg width="18" height="18" viewBox="0 0 24 24" fill="none" stroke="#fff" stroke-width="2"><circle cx="12" cy="12" r="10"/><path d="M9 7l2 3-1.5 1.5a8 8 0 003 3L14 13l3 2-1 2c-4 0-9-5-9-9z" fill="#fff" stroke="none"/></svg>
      1800.555.0142
    </div>
    <div class="item">
      <svg width="18" height="18" viewBox="0 0 24 24" fill="none" stroke="#fff" stroke-width="2"><circle cx="12" cy="12" r="10"/><rect x="7" y="8.5" width="10" height="7"/></svg>
      info@corventadx.com
    </div>
    <div class="social"><i></i><i></i><i></i></div>
  </div>
  <div class="brand" style="left:66px;top:84px"><span class="mark"></span>Corventa Dx</div>
  <nav class="nav">
    <span class="active">HOME</span><span>ABOUT</span><span>SERVICES</span><span>CLIENTS</span><span>NEWS</span><span>TESTIMONIALS</span><span>CONTACT</span>
  </nav>
</header>

<section class="hero" role="img" aria-label="Hospital laboratory scene with a hand holding a tablet showing diagnostic data">
  <p>We are a consulting firm that will serve medical diagnostics industry, which is part of the life science/healthcare industry focusing on developing and marketing products that help in early detection, monitoring or management of diseases.</p>
  <div class="btn" style="left:478px;top:342px;width:244px;height:48px;font-size:16px">GET STARTED</div>
</section>

<section class="about">
  <h2 class="heading" style="top:90px">ABOUT <span style="font-weight:500;color:var(--ink)">Corventa</span> <span>DX</span></h2>
  <p class="body-text">Lorem ipsum dolor sit amet, consectetuer adipiscing elit, sed diam nonummy nibh euismod tincidunt ut laoreet dolore magna aliquam erat volutpat. Ut wisi enim ad minim veniam, quis nostrud exerci tation ullamcorper suscipit lobortis nisl ut aliquip ex ea commodo consequat. Duis autem veleum iriure dolor in hendrerit in vul putate velit esse molestie consequat, vel illum dolore eu feugiat nulla facilisis at vero eros et accumsan.</p>
  <div class="btn" style="left:513px;top:333px;width:176px;height:42px;font-size:12px">LEARN MORE</div>
</section>

<section class="services">
  <h2 class="heading" style="top:96px">OUR <span>Services</span></h2>
  <svg class="arrow" style="left:58px;top:284px" width="30" height="30" viewBox="0 0 30 30"><circle cx="15" cy="15" r="15" fill="var(--blue)"/><path d="M18 9l-6 6 6 6" stroke="#fff" stroke-width="3" fill="none"/></svg>
  <svg class="arrow" style="left:1112px;top:284px" width="30" height="30" viewBox="0 0 30 30"><circle cx="15" cy="15" r="15" fill="var(--blue)"/><path d="M12 9l6 6-6 6" stroke="#fff" stroke-width="3" fill="none"/></svg>
  <div class="card" style="left:125px">
    <div class="photo" role="img" aria-label="Blue liquid test tubes in a laboratory rack" style="background:linear-gradient(160deg,#dbe9f2,#3aa4d8 55%,#1e6e9e)"></div>
    <h4>New Product Design</h4>
    <p>Lorem ipsum dolor sit amet, con sectetuer adipiscing elit, sed diam nonummy nibh euismod.</p>
  </div>
  <div class="card" style="left:448px">
    <div class="photo" role="img" aria-label="Laboratory microscope close-up" style="background:linear-gradient(160deg,#c9d6de,#7e93a2 55%,#3d4b56)"></div>
    <h4>New Product Evaluation</h4>
    <p>Lorem ipsum dolor sit amet, con sectetuer adipiscing elit, sed diam nonummy nibh euismod.</p>
  </div>
  <div class="card" style="left:772px">
    <div class="photo" role="img" aria-label="Businessman on a field looking ahead with a telescope" style="background:linear-gradient(180deg,#dbe4ec,#9db3c6 60%,#5a5e4c)"></div>
    <h4>Product Marketing</h4>
    <p>Lorem ipsum dolor sit amet, con sectetuer adipiscing elit, sed diam nonummy nibh euismod.</p>
  </div>
</section>

<section class="clients">
  <h2 class="heading" style="top:88px">OUR <span>Clients</span></h2>
  <div class="client-row">
    <span>NOVALT</span><span>KESTA</span><span>TRIVEON</span><span>BRIGHTMETRIC</span><span>HALDEN</span>
  </div>
</section>

<section class="news">
  <h2 class="heading" style="top:86px">Latest <span>News</span></h2>
  <div class="tile" role="img" aria-label="Doctor using a tablet" style="left:75px;top:204px;width:415px;height:413px;background:linear-gradient(135deg,#eef2f5,#b7c6d2 60%,#6c7f8f)"></div>
  <div class="tile" style="left:490px;top:204px;width:635px;height:187px;padding:28px 26px">
    <div class="date">January 03, 2019</div>
    <p>Lorem ipsum dolor sit amet, consectetuer adipiscing elit. Sed diam nonummy nibh euismod tincidunt ut laoreet dolore magna aliquam erat volutpat.</p>
    <svg class="dot-arrow" viewBox="0 0 22 22"><circle cx="11" cy="11" r="11" fill="var(--blue)"/><path d="M9 6l5 5-5 5" stroke="#fff" stroke-width="2.5" fill="none"/></svg>
  </div>
  <div class="tile" style="left:490px;top:398px;width:352px;height:219px;padding:44px 26px">
    <div class="date">February 24, 2019</div>
    <p>Lorem ipsum dolor sit amet. Sed diam nonummy nibh euis mod tincidunt ut laoreet dolore.</p>
    <svg class="dot-arrow" viewBox="0 0 22 22"><circle cx="11" cy="11" r="11" fill="var(--blue)"/><path d="M9 6l5 5-5 5" stroke="#fff" stroke-width="2.5" fill="none"/></svg>
  </div>
  <div class="tile" role="img" aria-label="Two businessmen reviewing documents" style="left:842px;top:398px;width:283px;height:219px;background:linear-gradient(135deg,#c6d4df,#5c7387 60%,#2a3642)"></div>
  <div class="tile" style="left:75px;top:627px;width:293px;height:277px;padding:72px 26px">
    <div class="date">March 19, 2019</div>
    <p>Lorem ipsum dolor sit am. Sed diam nonummy nibh euismod tincidunt ut.</p>
    <svg class="dot-arrow" viewBox="0 0 22 22"><circle cx="11" cy="11" r="11" fill="var(--blue)"/><path d="M9 6l5 5-5 5" stroke="#fff" stroke-width="2.5" fill="none"/></svg>
  </div>
  <div class="tile" role="img" aria-label="Finger touching a glowing data screen" style="left:368px;top:627px;width:528px;height:277px;background:linear-gradient(135deg,#3a2a5c,#1c3f7a 50%,#0e1a36)"></div>
  <div class="tile all-news" style="left:896px;top:627px;width:229px;height:277px">VIEW<br>ALL NEWS</div>
</section>

<section class="testimonials">
  <h2 class="heading" style="top:96px">Testimonials</h2>
  <div class="quote" style="left:92px;top:204px;width:476px;height:182px">Lorem ipsum dolor sit amet, consectetur adipiscing elit, sed do eiusmod tempor incididunt ut labore et dolore magna aliqua. Ut enim ad minim veniam, quis nostrud exercitation ullamco laboris nisi ut aliquip ex. Duis aute irure dolor in reprehenderit in voluptate velit esse.</div>
  <div class="person" style="left:104px;top:414px"><div class="avatar" role="img" aria-label="Client portrait"></div>Marina Holt</div>
  <div class="quote" style="left:590px;top:261px;width:518px;height:182px;padding-top:32px">Lorem ipsum dolor sit amet, consectetur adipiscing elit, sed do eiusmod tempor incididunt ut labore et dolore magna aliqua. Ut enim ad minim veniam, quis nostrud exercitation ullamco laboris nisi ut aliquip ex. Duis aute irure dolor in reprehenderit in voluptate velit esse.</div>
  <div class="person" style="left:606px;top:469px"><div class="avatar" role="img" aria-label="Client portrait"></div>Laura Pennick</div>
  <div class="dots"><i></i><i></i><i></i><i></i></div>
</section>

<section class="contact">
  <h2 class="heading" style="top:40px;left:448px">Send <span>a Message</span></h2>
  <h2 class="heading left" style="top:40px;left:922px">Contact <span>Us</span></h2>
  <div class="field" style="left:75px;top:130px;width:241px;height:44px">Your Name</div>
  <div class="field" style="left:329px;top:130px;width:239px;height:44px">Your Email</div>
  <div class="field" style="left:583px;top:130px;width:239px;height:44px">Your Subject</div>
  <div class="field msg" style="left:75px;top:189px;width:747px;height:135px">Message</div>
  <div class="btn" style="left:346px;top:339px;width:204px;height:40px;font-size:13px;border-radius:3px">Send Message</div>
  <div class="info">
    <div class="row">
      <svg width="16" height="16" viewBox="0 0 24 24" fill="none" stroke="#333" stroke-width="2"><circle cx="12" cy="12" r="10"/><path d="M12 6a4 4 0 00-4 4c0 3 4 7 4 7s4-4 4-7a4 4 0 00-4-4z"/></svg>
      <div>Corventa Dx<br>48 Sample Avenue<br>Suite #210<br>Philadelphia, PA 19103</div>
    </div>
    <div class="row">
      <svg width="16" height="16" viewBox="0 0 24 24" fill="none" stroke="#333" stroke-width="2"><circle cx="12" cy="12" r="10"/><path d="M9 7l2 3-1.5 1.5a8 8 0 003 3L14 13l3 2-1 2c-4 0-9-5-9-9z"/></svg>
      <div>1800-555-0142</div>
    </div>
    <div class="row">
      <svg width="16" height="16" viewBox="0 0 24 24" fill="none" stroke="#333" stroke-width="2"><circle cx="12" cy="12" r="10"/><rect x="7" y="8.5" width="10" height="7"/></svg>
      <div>info@corventadx.com</div>
    </div>
  </div>
</section>

<footer class="footer">
  <div class="brand" style="left:520px;top:115px"><span class="mark"></span>Corventa Dx</div>
  <div class="col" style="left:157px">
    <h5>QUICK LINKS</h5>
    Home<br>About<br>Services<br>Clients<br>News<br>Testimonials<br>Contact
  </div>
  <div class="col" style="left:349px">
    <h5>SERVICES</h5>
    New Product Design<br>New Product Evaluation<br>Product Marketing
  </div>
  <div class="col" style="left:585px">
    <h5>FOLLOW US</h5>
    <div class="s"><i></i>Friendlane</div>
    <div class="s"><i></i>Chirpline</div>
    <div class="s"><i></i>Workmesh</div>
  </div>
  <div class="col" style="left:789px">
    <h5 style="width:255px">NEWSLETTER SIGN UP</h5>
    Register your email address to get<br>more information about us
    <div class="subscribe-field">Email Address</div>
    <div class="btn" style="position:relative;width:130px;height:30px;font-size:11px;border-radius:15px;margin-top:10px">SUBSCRIBE</div>
  </div>
</footer>

<div class="abs copyright" style="left:0;width:1200px">COPYRIGHT © 2019 CORVENTA DX. ALL RIGHTS RESERVED.</div>

</body>
</html>
```